I want a business card that is going to show a creative spark but without limiting me to an industry. Something edgy but that wont go out of date. I want it state My business name Serafina Loire, profession - Professional Makeup Artist contact number and email

My service is to provide makeup services from bridal, fashion, photography, film, TV and so on. It is creative and different so i want that to be reflected.

I would like the card double sided.
Updates

 I would LOVE a background on my card something like this image... i can supply an image to be formed like this

Please use the image uploaded

Can we try using the image provided on one side of the card and then writing and details on the other side

Target Market(s)

I am targeting a wide range of people from Creative directors to the individual eg. bride

Industry/Entity Type

Business

Requirements
Must have
• Name: Delphine Hartwell
contact numbe 0417853120
email address:info@serafinaloire.com
website: www.serafinaloire.com
One of the images attached

professional makeup artist / hair stylist

I want it to show creativity
Nice to have
• logo, Double-sided card
Should not have
• the design should not use tradional style. Or images that are not my own

```html
<!DOCTYPE html>
<html lang="en">
<head>
<meta charset="utf-8">
<title>Serafina Loire — Business Card</title>
<link rel="stylesheet" href="https://fonts.googleapis.com/css2?family=Inter:wght@300;400&family=Roboto+Condensed:wght@300&display=swap">
<style>
  :root {
    --paper: #ffffff;
    --front-ink: #231f20;
    --back-grey: #808184;
    --white: #ffffff;
    --logo-grey: #a7a8aa;
    --muted: #c4c5c7;
    --label: #b4b5b7;
    --crop: #231f20;
    --photo-light: #9a9a9a;
    --photo-dark: #3a3a3a;
  }
  * { margin: 0; padding: 0; box-sizing: border-box; }
  html, body { width: 960px; height: 1200px; overflow: hidden; background: var(--paper); }
  body { position: relative; font-family: "Inter", Arial, sans-serif; }

  .crop-marks { position: absolute; inset: 0; width: 960px; height: 1200px; }
  .crop-marks line { stroke: var(--crop); stroke-width: 1.2; }

  .card { position: absolute; left: 45px; width: 868px; overflow: hidden; }

  .card-front { top: 61px; height: 475px; background: var(--front-ink); }
  .front-mark {
    position: absolute; left: 0; top: 160px; width: 480px; text-align: center;
    font-weight: 300; font-size: 52px; color: var(--logo-grey); letter-spacing: 1px;
  }
  .front-wordmark {
    position: absolute; left: 0; top: 280px; width: 480px; text-align: center;
    font-weight: 400; font-size: 17px; color: var(--white); letter-spacing: 9px;
  }
  .portrait {
    position: absolute; left: 498px; top: 0; width: 319px; height: 475px;
    background: radial-gradient(ellipse at 55% 45%, var(--photo-light) 0%, #6c6c6c 55%, var(--photo-dark) 100%);
  }
  .front-edge {
    position: absolute; left: 817px; top: 0; width: 2px; height: 475px; background: #555557;
  }

  .card-back { top: 652px; height: 476px; background: var(--back-grey); color: var(--white); }
  .website { position: absolute; right: 44px; top: 46px; font-weight: 300; font-size: 21px; }
  .identity { position: absolute; left: 84px; top: 140px; }
  .identity .name { font-weight: 300; font-size: 23px; }
  .identity .role {
    margin-top: 6px; font-family: "Roboto Condensed", "Arial Narrow", sans-serif;
    font-weight: 300; font-size: 16px; color: var(--muted); letter-spacing: 0.3px;
  }
  .contact { position: absolute; left: 84px; top: 282px; list-style: none; }
  .contact li { display: flex; align-items: baseline; font-weight: 300; font-size: 21px; margin-bottom: 10px; }
  .contact .label { width: 28px; font-size: 11px; color: var(--label); }
  .back-mark {
    position: absolute; right: 20px; bottom: 0; text-align: left;
    font-weight: 300; font-size: 78px; line-height: 0.9; color: var(--white);
  }
</style>
</head>
<body>
  <svg class="crop-marks" viewBox="0 0 960 1200" aria-hidden="true">
    <line x1="45" y1="12" x2="45" y2="46"/><line x1="913" y1="12" x2="913" y2="46"/>
    <line x1="0" y1="61" x2="32" y2="61"/><line x1="928" y1="61" x2="960" y2="61"/>
    <line x1="0" y1="536" x2="32" y2="536"/><line x1="928" y1="536" x2="960" y2="536"/>
    <line x1="45" y1="551" x2="45" y2="580"/><line x1="913" y1="551" x2="913" y2="580"/>
    <line x1="45" y1="610" x2="45" y2="638"/><line x1="913" y1="610" x2="913" y2="638"/>
    <line x1="0" y1="652" x2="32" y2="652"/><line x1="928" y1="652" x2="960" y2="652"/>
    <line x1="0" y1="1128" x2="32" y2="1128"/><line x1="928" y1="1128" x2="960" y2="1128"/>
    <line x1="45" y1="1143" x2="45" y2="1185"/><line x1="913" y1="1143" x2="913" y2="1185"/>
  </svg>

  <section class="card card-front">
    <div class="front-mark">Serafina Loire</div>
    <div class="front-wordmark">SERAFINA LOIRE</div>
    <div class="portrait" role="img" aria-label="Black and white beauty portrait of a model with sleek short hair"></div>
    <div class="front-edge"></div>
  </section>

  <section class="card card-back">
    <div class="website">www.serafinaloire.com</div>
    <div class="identity">
      <div class="name">Serafina Loire</div>
      <div class="role">PROFESSIONAL MAKE UP ARTIST + HAIRSTYLIST</div>
    </div>
    <ul class="contact">
      <li><span class="label">T</span>0417853120</li>
      <li><span class="label">E</span>info@serafinaloire.com</li>
    </ul>
    <div class="back-mark">Serafina<br>Loire</div>
  </section>
</body>
</html>
```